Business Card for Quillmark Ledger - A cannabis publication for executives.

I'd like some business cards for Quillmark Ledger. The logo is done (great job!) and I need a card design I will use with PRINTLY. I made it a short project to allow time for printing before an event. These will be standard sized cards (final artwork size 3.66" x 2.16" at 300dpi) with a final card size of 3.5" x 2.0". (See PRINTLY.com if you need more info.) I might try rounded corners but am not sure yet. I think the design will work okay with rounded.

Quillmark Ledger will be a bi-weekly publication for the cannabis industry. It is targeted to investors and industry executives, not consumers or pot smokers. So our market is more B2B. However I am open to creativity and making the card something people remark on.

My contact for card:

Dana Merrow
Founder/CEO
dana@quillmarkledger.example

2740 Harlow Avenue
Boston MA 02135
(617)555-0194

Target Market(s)

Executives, Industry people and investors in the Cannabis sector.

Contact Information for Business Card

PRINTLY does do double sided and the second side can be the same or different images. Only one side is required but use of the second side would be a bonus.

Font styles to use
Serif
Sans Serif
Decorative

Colors

Designer to choose colors to be used in the design.

Requirements
Must have
• Logo, contact info
Nice to have
• Style and design to make the card stand out in a crowd.

```html
<!DOCTYPE html>
<html lang="en">
<head>
<meta charset="utf-8">
<title>Quillmark Ledger — Business Card</title>
<link href="https://fonts.googleapis.com/css2?family=Tinos:wght@400;700&display=swap" rel="stylesheet">
<style>
  :root {
    --backdrop: #e4e5e7;
    --card: #ffffff;
    --brand-blue: #1769c4;
    --brand-green: #79b52a;
    --card-shadow: 0 10px 28px rgba(0,0,0,0.16);
  }
  * { box-sizing: border-box; margin: 0; padding: 0; }
  html, body { width: 1200px; height: 800px; overflow: hidden; }
  body {
    background: var(--backdrop);
    font-family: "Tinos", "Times New Roman", serif;
    display: flex;
    flex-direction: column;
    align-items: center;
    justify-content: center;
    gap: 36px;
  }
  .card {
    width: 630px;
    height: 360px;
    background: var(--card);
    box-shadow: var(--card-shadow);
    position: relative;
  }

  /* Front side */
  .card-front {
    display: flex;
    align-items: center;
    justify-content: center;
  }
  .wordmark {
    display: flex;
    align-items: center;
    gap: 18px;
    color: var(--brand-blue);
    font-weight: 700;
  }
  .wordmark-square {
    width: 58px;
    height: 58px;
    background: var(--brand-green);
  }
  .wordmark-name { font-size: 52px; letter-spacing: -0.5px; }

  /* Back side */
  .card-back { display: flex; }
  .contact-panel {
    width: 56%;
    padding: 44px 0 0 38px;
  }
  .wordmark-small { gap: 10px; margin-bottom: 22px; }
  .wordmark-small .wordmark-square { width: 30px; height: 30px; }
  .wordmark-small .wordmark-name { font-size: 28px; }
  .contact-list { list-style: none; color: var(--brand-blue); font-size: 17px; line-height: 1.35; }
  .contact-list li { display: flex; align-items: flex-start; gap: 9px; margin-bottom: 4px; }
  .contact-icon { flex: none; width: 18px; height: 18px; margin-top: 2px; }
  .divider {
    width: 2px;
    background: var(--brand-green);
    margin: 78px 0;
  }
  .person-panel {
    flex: 1;
    display: flex;
    align-items: center;
    padding-left: 36px;
    gap: 14px;
  }
  .person-badge {
    width: 36px; height: 36px; border-radius: 50%;
    background: var(--brand-green);
    flex: none;
  }
  .person-name { color: var(--brand-blue); font-size: 30px; line-height: 1.1; }
  .person-title { color: var(--brand-green); font-size: 17px; }
</style>
</head>
<body>
  <section class="card card-front" aria-label="Card front">
    <div class="wordmark">
      <span class="wordmark-square"></span>
      <span class="wordmark-name">Quillmark Ledger</span>
    </div>
  </section>

  <section class="card card-back" aria-label="Card back">
    <div class="contact-panel">
      <div class="wordmark wordmark-small">
        <span class="wordmark-square"></span>
        <span class="wordmark-name">Quillmark Ledger</span>
      </div>
      <ul class="contact-list">
        <li>
          <svg class="contact-icon" viewBox="0 0 18 18" aria-hidden="true">
            <circle cx="9" cy="9" r="8" fill="none" stroke="#79b52a" stroke-width="1.4"/>
            <rect x="6.2" y="4" width="5.6" height="10" rx="1" fill="none" stroke="#79b52a" stroke-width="1.2"/>
          </svg>
          <span>(617)555-0194</span>
        </li>
        <li>
          <svg class="contact-icon" viewBox="0 0 18 18" aria-hidden="true">
            <circle cx="9" cy="9" r="8" fill="none" stroke="#79b52a" stroke-width="1.4"/>
            <rect x="4.5" y="6" width="9" height="6.5" fill="none" stroke="#79b52a" stroke-width="1.2"/>
            <path d="M4.5 6 L9 9.8 L13.5 6" fill="none" stroke="#79b52a" stroke-width="1.2"/>
          </svg>
          <span>dana@quillmarkledger.example</span>
        </li>
        <li>
          <svg class="contact-icon" viewBox="0 0 18 18" aria-hidden="true">
            <circle cx="9" cy="9" r="8" fill="none" stroke="#79b52a" stroke-width="1.4"/>
            <path d="M4.5 9 L9 5 L13.5 9 M6 8 V13 H12 V8" fill="none" stroke="#79b52a" stroke-width="1.2"/>
          </svg>
          <span>2740 Harlow Avenue<br>Boston MA 02135</span>
        </li>
      </ul>
    </div>
    <div class="divider"></div>
    <div class="person-panel">
      <span class="person-badge"></span>
      <div>
        <p class="person-name">Dana Merrow</p>
        <p class="person-title">Founder/CEO</p>
      </div>
    </div>
  </section>
</body>
</html>
```